Single page 8 1/2 x 11 flyer to entice new homeowners to visit our WEBSITE

A single page flyer that we can put on an easel that promotes our website, tallowpine58.com, to new homeowners for blinds, shades, bath hardware, cabinet organization, etc. This piece will be on an easel in sales centers, design studios and closing offices. We want the homeowners to know where they can go to get reliable products and service from a trusted partner of their builder for products that were not installed in their new home before they closed.

Enter the coupon code KQT10 to get 10% off of your entire purchase and free shipping. The product on our website will put the finishing touches on their home. ....make your house your home

Target Market(s)

New homebuyers

Industry/Entity Type

Residential Construction

Font styles to use
Serif

Colors
ec1f27

Requirements
Must have
• Logo and website, tallowpine58.com and tagline, make your house your home
Nice to have
• what will drive new homeowners to the website to purchase items they did not purchase before closing like window blinds and shades, bath hardware, ceiling fans, grills, electric fireplaces, etc.

```html
<!DOCTYPE html>
<html lang="en">
<head>
<meta charset="utf-8">
<title>Tallow Pine 58 – Make Your House Your Home</title>
<link rel="stylesheet" href="https://fonts.googleapis.com/css2?family=Questrial&family=Open+Sans:wght@400;700;800&display=swap">
<style>
  :root {
    --red: #e0121a;
    --ink: #141414;
    --white: #ffffff;
    --grey: #8a8a8a;
    --stage: #eceef1;
    --tape: rgba(240, 190, 175, 0.75);
  }
  * { box-sizing: border-box; margin: 0; padding: 0; }
  html, body { width: 1200px; height: 1200px; overflow: hidden; background: var(--stage); }
  .flyer {
    position: absolute; left: 136px; top: 0; width: 927px; height: 1200px;
    background: var(--white); overflow: hidden;
    font-family: "Questrial", sans-serif; color: var(--ink);
  }
  .brand { position: absolute; left: 53px; top: 70px; display: flex; align-items: center; gap: 14px; }
  .brand-dot { width: 58px; height: 58px; border-radius: 50%; background: var(--red); }
  .brand-name { font-size: 40px; letter-spacing: 1px; color: var(--ink); }
  .contact { position: absolute; right: 53px; top: 78px; text-align: right; }
  .contact-phone { font-size: 27px; color: var(--red); line-height: 34px; }
  .contact-web { font-size: 27px; color: var(--ink); line-height: 34px; }
  .rule { position: absolute; left: 0; top: 197px; width: 100%; height: 10px; background: var(--red); }
  .hero-photo {
    position: absolute; left: 0; top: 207px; width: 100%; height: 505px;
    background: linear-gradient(100deg, #f6f5f3 0%, #efece7 45%, #e4ddd3 70%, #d9d6d2 100%);
  }
  .tagline { position: absolute; left: 64px; top: 280px; font-size: 78px; line-height: 72px; font-weight: 400; }
  .tagline .red { color: var(--red); }
  .tagline .dark { color: var(--ink); }
  .band { position: absolute; left: 0; top: 712px; width: 100%; height: 399px; background: var(--red); }
  .band-title {
    position: absolute; left: 60px; top: 770px; font-size: 64px; line-height: 72px; font-weight: 400;
    color: var(--white); white-space: nowrap;
  }
  .band-rule { position: absolute; left: 55px; top: 850px; width: 562px; height: 2px; background: var(--white); }
  .offer-head {
    position: absolute; left: 100px; width: 480px; top: 865px; text-align: center;
    font-size: 26px; color: var(--ink); white-space: nowrap;
  }
  .offer-copy {
    position: absolute; left: 90px; width: 500px; top: 902px; text-align: center;
    font-size: 16px; line-height: 18.5px; color: var(--white);
  }
  .offer-copy p + p { margin-top: 17px; }
  .badge {
    position: absolute; left: 665px; top: 619px; width: 212px; height: 212px; border-radius: 50%;
    background: var(--white); border: 3px solid var(--red);
    box-shadow: 0 0 0 5px var(--white);
    display: flex; flex-direction: column; align-items: center; justify-content: center;
    transform: rotate(15deg); font-family: "Open Sans", sans-serif; text-align: center;
  }
  .badge-deal { color: var(--red); font-weight: 800; font-size: 30px; line-height: 31px; }
  .badge-code { color: var(--grey); font-size: 20px; line-height: 23px; margin-top: 8px; }
  .product-card {
    position: absolute; left: 613px; top: 925px; width: 270px; height: 155px;
    background: var(--white); padding: 8px; transform: rotate(22deg);
  }
  .product-photo { width: 100%; height: 100%; background: linear-gradient(90deg, #d9ddd2 0%, #eef0e6 45%, #b7b3a6 80%, #6f5a48 100%); }
  .product-label {
    position: absolute; left: -6px; bottom: 18px; background: var(--red); color: var(--white);
    font-size: 15px; padding: 2px 12px; white-space: nowrap;
  }
  .tape { position: absolute; width: 95px; height: 20px; background: var(--tape); }
  .tape-top { left: 612px; top: 895px; transform: rotate(-10deg); }
  .tape-bottom { left: 805px; top: 1115px; transform: rotate(-10deg); }
  .bath-circle {
    position: absolute; left: 23px; top: 1009px; width: 120px; height: 120px; border-radius: 50%;
    background: var(--white);
  }
  .bath-photo { position: absolute; left: 25px; top: 25px; width: 70px; height: 70px; border-radius: 50%; background: radial-gradient(circle, #d6d8da 0%, #f4f4f4 70%); }
  .bath-label {
    position: absolute; left: 40px; top: 1095px; background: var(--red); color: var(--white);
    font-size: 15px; padding: 2px 10px; transform: rotate(-25deg); white-space: nowrap;
  }
  .footer { position: absolute; left: 0; width: 100%; top: 1127px; text-align: center; font-size: 19px; line-height: 21px; }
</style>
</head>
<body>
  <main class="flyer">
    <header>
      <div class="brand"><span class="brand-dot"></span><span class="brand-name">TALLOW PINE 58</span></div>
      <div class="contact">
        <div class="contact-phone">(555) 014-2286</div>
        <div class="contact-web">www.tallowpine58.com</div>
      </div>
    </header>
    <div class="rule"></div>
    <div class="hero-photo" role="img" aria-label="Bright white living room with wicker sofa, fireplace and driftwood decor"></div>
    <h1 class="tagline">
      <span class="red">MAKE</span><br><span class="dark">YOUR</span><br><span class="red">HOUSE</span><br><span class="dark">YOUR</span><br><span class="red">HOME</span>
    </h1>
    <section class="band"></section>
    <h2 class="band-title">TALLOW PINE 58</h2>
    <div class="band-rule"></div>
    <div class="offer-head">10% OFF YOUR ENTIRE PURCHASE</div>
    <div class="offer-copy">
      <p>Your builder and their trusted suppliers have<br>partnered together to offer you this special opportunity.</p>
      <p>Go to www.tallowpine58.com and shop for<br>your window coverings, ceiling fans, cabinet and<br>closet organization, bath hardware and more.</p>
      <p>During Checkout, enter promo code KQT10<br>and get a 10% discount on your entire purchase</p>
    </div>
    <div class="badge">
      <div class="badge-deal">10% off<br>your entire<br>purchase!</div>
      <div class="badge-code">use promo<br>code KQT10</div>
    </div>
    <div class="tape tape-top"></div>
    <div class="product-card">
      <div class="product-photo" role="img" aria-label="Sheer vertical window blinds in a furnished room"></div>
      <span class="product-label">Window Coverings</span>
    </div>
    <div class="tape tape-bottom"></div>
    <div class="bath-circle"><div class="bath-photo" role="img" aria-label="Chrome towel ring bath fixture"></div></div>
    <span class="bath-label">Bath Hardware</span>
    <footer class="footer">
      <div>CALL US: (555) 014-2286</div>
      <div>Visit us online: www.tallowpine58.com</div>
    </footer>
  </main>
</body>
</html>
```